Consulting company business cards

We have a base design, but would be willing to update. We have a new logo/"tag" that needs to be added. Current business card design is attached for reference into our "style."

Industry/Entity Type

Business

Contact Information for Business Card

Should contain name and title, office number, mobile number if appropriate, e-mail, website, physical address, and company logo.

Font styles to use
Other font styles liked:
• See current card design on GorvandBCard

Colors
0455a3
85acd3
aaaaaa

Requirements
Must have
• Our colors are navy blue, gray, and a lighter blue
Nice to have
• Design that I can easily drop in new names/titles as we hire employees.

```html
<!DOCTYPE html>
<html lang="en">
<head>
<meta charset="utf-8">
<title>Harlow Business Cards</title>
<link rel="stylesheet" href="https://fonts.googleapis.com/css2?family=Lato:wght@400;700;900&display=swap">
<style>
  :root {
    --navy: #0f2d4a;
    --blue: #0455a3;
    --blue-mid: #1a6fbd;
    --blue-sky: #2a9fd8;
    --blue-light: #85acd3;
    --grey: #aaaaaa;
    --grey-light: #d6d6d6;
    --ink: #222222;
    --paper: #ffffff;
    --backdrop: #ececec;
  }
  * { box-sizing: border-box; margin: 0; padding: 0; }
  html, body {
    width: 1200px; height: 900px; overflow: hidden;
    background: var(--backdrop);
    font-family: "Lato", Arial, sans-serif;
  }
  .canvas { position: relative; width: 1200px; height: 900px; }

  .card {
    position: absolute;
    width: 520px; height: 300px;
    background: var(--paper);
    box-shadow: 0 6px 18px rgba(0,0,0,0.12);
    overflow: hidden;
  }

  /* Banded logo card */
  .card--banded { left: 340px; top: 90px; }
  .band {
    position: absolute; left: 0; width: 100%; height: 34px;
    background: linear-gradient(90deg, var(--blue) 0%, var(--blue-mid) 55%, var(--blue-sky) 100%);
  }
  .band--top { top: 0; }
  .band--bottom { bottom: 0; background: linear-gradient(90deg, var(--blue-sky) 0%, var(--blue-mid) 45%, var(--blue) 100%); }

  .brand {
    position: absolute; left: 50%; top: 50%;
    transform: translate(-50%, -50%);
    text-align: left;
  }
  .brand__row { display: flex; align-items: center; gap: 12px; }
  .brand__name {
    font-weight: 900; font-size: 64px; letter-spacing: 3px;
    color: var(--navy); line-height: 1;
  }
  .brand__dot {
    width: 46px; height: 46px; border-radius: 50%;
    background: var(--blue-light);
  }
  .brand__tagline {
    margin-top: 6px;
    font-size: 15px; letter-spacing: 2.4px;
    color: var(--grey);
  }

  /* Plain logo card */
  .card--logo { left: 60px; top: 500px; }

  /* Contact card */
  .card--contact { left: 620px; top: 500px; }
  .strip {
    position: absolute; left: 0; top: 0; width: 48px; height: 100%;
    display: flex; flex-direction: column;
  }
  .strip__texture {
    flex: 1;
    background: linear-gradient(160deg, var(--grey-light) 0%, var(--grey) 50%, var(--grey-light) 100%);
  }
  .strip__icon {
    height: 44px; display: flex; align-items: center; justify-content: center;
  }
  .strip__icon svg { width: 20px; height: 20px; fill: #fff; }
  .strip__icon--1 { background: var(--blue-sky); }
  .strip__icon--2 { background: #238ccd; }
  .strip__icon--3 { background: var(--blue-mid); }
  .strip__icon--4 { background: var(--blue); }

  .details { position: absolute; left: 78px; top: 44px; width: 240px; color: var(--ink); }
  .details__name { font-weight: 700; font-size: 22px; letter-spacing: 0.5px; }
  .details__title { font-size: 15px; color: var(--blue-sky); letter-spacing: 0.5px; margin-top: 1px; }
  .details__rule { height: 2px; background: var(--blue-mid); margin: 5px 0 7px; }
  .details__group { font-size: 16px; line-height: 1.2; }
</style>
</head>
<body>
<main class="canvas">

  <section class="card card--banded">
    <div class="band band--top"></div>
    <div class="brand">
      <div class="brand__row"><span class="brand__name">HARLOW</span><span class="brand__dot"></span></div>
      <p class="brand__tagline">A CLOUD CONSULTING COMPANY</p>
    </div>
    <div class="band band--bottom"></div>
  </section>

  <section class="card card--logo">
    <div class="brand">
      <div class="brand__row"><span class="brand__name">HARLOW</span><span class="brand__dot"></span></div>
      <p class="brand__tagline">A CLOUD CONSULTING COMPANY</p>
    </div>
  </section>

  <section class="card card--contact">
    <div class="strip">
      <div class="strip__texture" role="img" aria-label="Grey faceted geometric pattern"></div>
      <div class="strip__icon strip__icon--1">
        <svg viewBox="0 0 20 20"><circle cx="10" cy="6" r="4"/><path d="M2 19c0-5 3.5-7 8-7s8 2 8 7z"/></svg>
      </div>
      <div class="strip__icon strip__icon--2">
        <svg viewBox="0 0 20 20"><path d="M5 1l3 4-2 2c1 3 3 5 6 6l2-2 4 3-2 4C8 18 2 12 1 4z"/></svg>
      </div>
      <div class="strip__icon strip__icon--3">
        <svg viewBox="0 0 20 20"><circle cx="10" cy="10" r="8" fill="none" stroke="#fff" stroke-width="2"/><path d="M2 10h16M10 2c3 3 3 13 0 16M10 2c-3 3-3 13 0 16" fill="none" stroke="#fff" stroke-width="1.5"/></svg>
      </div>
      <div class="strip__icon strip__icon--4">
        <svg viewBox="0 0 20 20"><path d="M10 1a6 6 0 0 1 6 6c0 5-6 12-6 12S4 12 4 7a6 6 0 0 1 6-6z"/><circle cx="10" cy="7" r="2.2" fill="#0455a3"/></svg>
      </div>
      <div class="strip__texture" role="img" aria-label="Grey faceted geometric pattern"></div>
    </div>

    <div class="details">
      <p class="details__name">EVAN MARLOCK</p>
      <p class="details__title">CEO DIRECTOR</p>
      <div class="details__rule"></div>
      <p class="details__group">+000 898 5845<br>+000 554 8888</p>
      <div class="details__rule"></div>
      <p class="details__group">name@email.com<br>www.website.com</p>
      <div class="details__rule"></div>
      <p class="details__group">Address Line 1<br>Address Line 2</p>
    </div>
  </section>

</main>
</body>
</html>
```